PRVD Traditional Business Card Project

Please see attached....just a simple business card... on attachment- please use the exact font, style, etc as the attached "Pat Everard Wynne" card... however, replace with the "Owen Reginald Talbot" text and address below the card.

```html
<!DOCTYPE html>
<html lang="en">
<head>
<meta charset="utf-8">
<title>PRVD Business Card</title>
<link rel="stylesheet" href="https://fonts.googleapis.com/css2?family=Noto+Serif:wght@400&display=swap">
<style>
  :root {
    --backdrop: #d3d3d3;
    --card: #ffffff;
    --ink: #111111;
  }
  * { margin: 0; padding: 0; box-sizing: border-box; }
  html, body {
    width: 1000px;
    height: 1200px;
    overflow: hidden;
    background: var(--backdrop);
  }
  .card {
    position: absolute;
    left: 40px;
    top: 149px;
    width: 919px;
    height: 528px;
    background: var(--card);
    color: var(--ink);
    font-family: "Noto Serif", Georgia, serif;
    font-weight: 400;
  }
  .card p { position: absolute; white-space: nowrap; line-height: 1; }
  .firm-name {
    left: 53px;
    top: 48px;
    font-size: 40px;
    font-variant: small-caps;
    letter-spacing: 0.5px;
  }
  .firm-suffix {
    left: 121px;
    top: 103px;
    font-size: 21px;
    letter-spacing: 2.5px;
  }
  .person-name {
    left: 0;
    width: 100%;
    text-align: center;
    top: 222px;
    font-size: 50px;
    font-variant: small-caps;
  }
  .person-title {
    left: 0;
    width: 100%;
    text-align: center;
    top: 284px;
    font-size: 22px;
    letter-spacing: 3px;
  }
  .contact {
    position: absolute;
    top: 398px;
    font-size: 23px;
    line-height: 33px;
    list-style: none;
    letter-spacing: 0.3px;
  }
  .contact-address { left: 53px; }
  .contact-lines { right: 50px; text-align: right; }
</style>
</head>
<body>
  <main class="card">
    <p class="firm-name">Pacific Ridge</p>
    <p class="firm-suffix">VALLEY DEFENSE GROUP, PLC</p>
    <p class="person-name">Owen Reginald Talbot</p>
    <p class="person-title">ATTORNEY AT LAW</p>
    <ul class="contact contact-address">
      <li>4127 CEDAR LANE, SUITE C</li>
      <li>ALDER SPRINGS, CA 90000</li>
      <li>www.lawprvd.com</li>
    </ul>
    <ul class="contact contact-lines">
      <li>TEL (555) 210-3300</li>
      <li>FAX (555) 210-3301</li>
      <li>otalbot@lawprvd.com</li>
    </ul>
  </main>
</body>
</html>
```